Hi Designers,

I will need 4 web pages designed. The web page looks like an App (if you click on the logo, or the icon on an iPad, it will take you to the website), but it is still a webpage.

Please check the attachment on this brief to understand what specific pages I need to be designed.

A .PSD (straight-up PhotoShop image) as final deliverable is fine, as long as you give us the exact “web color numbers”.

The design is for desktop and iPad but in a single unified web application, NOT separate web app and (native) iPad app.

Details:

Bright Harbor Policy Systems is developing a browser-based application for use on any mobile device or desktop. The app will be used by corporations to communicate with their employees regarding legal, regulatory and company requirements for conducting business. The app is known as “Workplace Guidance Hub.” When the user clicks on the icon for Workplace Guidance Hub, they will enter a site full of information that a company deems necessary for the employee to do his/her job. There are several content sections within the site, including a login page, training, policies, forms, news feeds and blogs.

The application has been built using Microsoft .NET, and fully supports CSS-type skinning; it uses traditional page layouts. We are seeking a product logo concept (image), a master application/desktop icon (image), as well as a full color scheme/theme/skin design for all areas of the application (header area, body text, menu bar, etc.) in the form of a CSS. The look should be clean, crisp and professional; nothing cartoony or whimsical. It should be easy to read and “airy”.

We have sketched prototypes for the basic application page layout that we can send as a next step of the process.
Updates

Screen shots have been uploaded to this project.  Please use them to guide your design.

Dear designers,

I apologize for the delay in providing feedback. My partners and I will provide feedback in a few days. Thank you for your patience.

Industry/Entity Type

Business

Font styles to use
Other font styles liked:
• see font on screen shots when uploaded

```html
<!DOCTYPE html>
<html lang="en">
<head>
<meta charset="utf-8">
<title>Workplace Guidance Hub — Dashboard</title>
<link rel="stylesheet" href="https://fonts.googleapis.com/css2?family=Open+Sans:wght@400;600;700&display=swap">
<style>
  :root {
    --page: #f4f4f4;
    --topbar: #e4e4e4;
    --sidebar: #ececec;
    --line: #d6d6d6;
    --text: #5e5e5e;
    --muted: #9a9a9a;
    --accent-red: #ec5a4f;
    --accent-teal: #3fcfb0;
    --accent-blue: #41b7e3;
    --accent-link: #3aa6d8;
    --date: #45c7a6;
    --board-head: #6c6c6c;
    --board-a: #dadada;
    --board-b: #cecece;
    --board-rank: #f7f7f7;
    --badge: #e84a3f;
    --white: #ffffff;
  }
  * { box-sizing: border-box; margin: 0; padding: 0; }
  html, body { width: 1200px; height: 900px; overflow: hidden; }
  body { font-family: "Open Sans", Arial, sans-serif; color: var(--text); background: var(--page); font-size: 12px; }

  .app { display: grid; grid-template-columns: 220px 1fr 300px; grid-template-rows: 52px 1fr; width: 1200px; height: 900px; }

  .topbar { grid-column: 1 / 4; background: var(--topbar); display: flex; align-items: center; padding: 0 20px; border-bottom: 1px solid var(--line); }
  .topbar-tabs { display: flex; gap: 46px; margin-left: 30px; }
  .tab-icon { position: relative; width: 26px; height: 22px; color: #8d8d8d; }
  .tab-badge { position: absolute; top: -6px; right: -8px; background: var(--badge); color: var(--white); font-size: 9px; font-weight: 700; width: 14px; height: 14px; line-height: 14px; text-align: center; border-radius: 2px; }
  .user { margin-left: auto; display: flex; align-items: center; gap: 10px; font-size: 12px; color: var(--text); }
  .user-avatar { width: 26px; height: 26px; background: linear-gradient(135deg, #b89a84, #e2d2c4); border: 2px solid var(--white); }

  .sidebar { background: var(--sidebar); border-right: 1px solid var(--line); padding: 14px 14px; overflow: hidden; }
  .sidebar-title { display: flex; align-items: center; gap: 8px; font-size: 13px; color: var(--text); margin-bottom: 12px; }
  .search { height: 26px; background: var(--white); border: 1px solid var(--line); border-radius: 2px; display: flex; align-items: center; gap: 6px; padding: 0 8px; color: var(--muted); font-size: 11px; margin-bottom: 18px; }
  .news-item { display: grid; grid-template-columns: 22px 1fr; gap: 10px; padding: 14px 0; border-bottom: 1px solid var(--line); }
  .news-icon { width: 20px; height: 22px; color: #9a9a9a; }
  .news-text { font-size: 11px; line-height: 1.45; color: var(--muted); }
  .news-link { display: block; margin-top: 10px; color: var(--accent-link); font-size: 11px; }

  .main { padding: 16px 18px; overflow: hidden; }
  .welcome { background: var(--white); margin-bottom: 16px; }
  .welcome-bar { background: var(--accent-red); color: var(--white); font-size: 13px; font-weight: 600; padding: 8px 14px 8px 90px; display: flex; align-items: center; gap: 8px; }
  .welcome-body { display: flex; gap: 16px; padding: 0 16px 14px; }
  .welcome-photo { width: 58px; height: 58px; margin-top: -30px; border: 3px solid var(--white); background: linear-gradient(135deg, #e9c98e, #c88b6b); flex: none; }
  .welcome-text { font-size: 11px; line-height: 1.55; color: var(--muted); padding-top: 8px; }

  .columns { display: grid; grid-template-columns: 1fr 1fr; gap: 16px; }
  .panel { background: var(--white); }
  .panel-head { color: var(--white); font-size: 13px; font-weight: 600; padding: 8px 14px; display: flex; align-items: center; gap: 8px; }
  .panel-head.whats-new { background: var(--accent-teal); }
  .panel-head.game { background: var(--accent-blue); }

  .update { display: grid; grid-template-columns: 40px 1fr; gap: 12px; padding: 13px 14px; border-bottom: 1px solid #ececec; }
  .update-thumb { width: 40px; height: 32px; background: linear-gradient(135deg, #9fb0bf, #d8dde2); }
  .update-date { color: var(--date); font-size: 11px; font-weight: 600; }
  .update-text { font-size: 10.5px; line-height: 1.45; color: var(--muted); }

  .feature { text-align: center; padding: 20px 24px 22px; border-bottom: 1px solid #e6e6e6; margin: 0 14px; }
  .feature:last-child { border-bottom: none; }
  .feature-head { display: flex; align-items: center; justify-content: center; gap: 14px; font-size: 13px; color: var(--text); margin-bottom: 10px; }
  .feature-icon { width: 22px; height: 22px; color: var(--accent-blue); }
  .feature-text { font-size: 10.5px; line-height: 1.45; color: var(--muted); }

  .leaderboard { background: var(--board-a); border-left: 1px solid var(--line); overflow: hidden; }
  .board-title { background: var(--board-head); color: var(--white); font-size: 13px; font-weight: 600; text-align: center; padding: 8px; }
  .board-cols, .board-row { display: grid; grid-template-columns: 40px 1fr 50px 60px; align-items: center; padding: 0 14px; }
  .board-cols { height: 28px; font-size: 10px; color: var(--muted); background: var(--board-a); }
  .board-row { height: 32px; font-size: 11px; color: var(--text); }
  .board-row:nth-child(odd) { background: var(--board-b); }
  .board-row:nth-child(even) { background: var(--board-a); }
  .rank { width: 16px; height: 16px; border-radius: 50%; background: var(--board-rank); font-size: 9px; text-align: center; line-height: 16px; color: var(--muted); }
</style>
</head>
<body>
<div class="app">
  <header class="topbar">
    <nav class="topbar-tabs">
      <span class="tab-icon"><svg viewBox="0 0 26 22" width="26" height="22" fill="none" stroke="currentColor" stroke-width="1.6"><rect x="2" y="3" width="20" height="16" rx="2"/><path d="M2 7h20"/></svg><span class="tab-badge">4</span></span>
      <span class="tab-icon"><svg viewBox="0 0 26 22" width="26" height="22" fill="none" stroke="currentColor" stroke-width="1.6"><rect x="4" y="2" width="16" height="18" rx="1"/><path d="M8 8h8M8 12h8M8 16h5"/></svg></span>
      <span class="tab-icon"><svg viewBox="0 0 26 22" width="26" height="22" fill="none" stroke="currentColor" stroke-width="1.6"><rect x="2" y="2" width="22" height="14" rx="1"/><path d="M9 20h8M13 16v4"/></svg></span>
      <span class="tab-icon"><svg viewBox="0 0 26 22" width="26" height="22" fill="none" stroke="currentColor" stroke-width="1.6"><path d="M5 11a8 8 0 0 1 14-5M21 11a8 8 0 0 1-14 5"/><path d="M19 2v4h-4M7 20v-4h4"/></svg></span>
    </nav>
    <div class="user">
      <span class="user-avatar" role="img" aria-label="User profile photo"></span>
      <span>Daniel Reyes</span>
      <svg width="8" height="6" viewBox="0 0 8 6"><path d="M0 0h8L4 6z" fill="#8d8d8d"/></svg>
    </div>
  </header>

  <aside class="sidebar">
    <h2 class="sidebar-title"><svg width="14" height="14" viewBox="0 0 14 14" fill="none" stroke="#8d8d8d" stroke-width="1.4"><path d="M2 2l10 10M12 2L2 12"/></svg>Industry News</h2>
    <div class="search"><svg width="11" height="11" viewBox="0 0 11 11" fill="none" stroke="#aaa" stroke-width="1.4"><circle cx="4.5" cy="4.5" r="3.5"/><path d="M7 7l3 3"/></svg>Search news</div>
    <article class="news-item"><svg class="news-icon" viewBox="0 0 20 22" fill="none" stroke="currentColor" stroke-width="1.4"><rect x="2" y="1" width="16" height="20" rx="1"/><path d="M6 7h8M6 11h8M6 15h5"/></svg><p class="news-text">Lorem ipsum dolor sit amet consectetur adipiscing elit sed do eiusmod tempor.<a class="news-link">monthly report summary</a></p></article>
    <article class="news-item"><svg class="news-icon" viewBox="0 0 20 22" fill="none" stroke="currentColor" stroke-width="1.4"><rect x="2" y="1" width="16" height="20" rx="1"/><path d="M6 7h8M6 11h8M6 15h5"/></svg><p class="news-text">Lorem ipsum dolor sit amet consectetur adipiscing elit sed do eiusmod tempor.<a class="news-link">monthly report summary</a></p></article>
    <article class="news-item"><svg class="news-icon" viewBox="0 0 20 22" fill="none" stroke="currentColor" stroke-width="1.4"><rect x="2" y="1" width="16" height="20" rx="1"/><path d="M6 7h8M6 11h8M6 15h5"/></svg><p class="news-text">Lorem ipsum dolor sit amet consectetur adipiscing elit sed do eiusmod tempor.<a class="news-link">monthly report summary</a></p></article>
    <article class="news-item"><svg class="news-icon" viewBox="0 0 20 22" fill="none" stroke="currentColor" stroke-width="1.4"><rect x="2" y="1" width="16" height="20" rx="1"/><path d="M6 7h8M6 11h8M6 15h5"/></svg><p class="news-text">Lorem ipsum dolor sit amet consectetur adipiscing elit sed do eiusmod tempor.<a class="news-link">monthly report summary</a></p></article>
  </aside>

  <main class="main">
    <section class="welcome">
      <h1 class="welcome-bar"><svg width="12" height="12" viewBox="0 0 12 12"><path d="M6 0l1.8 4H12L8.6 6.6 10 12 6 8.8 2 12l1.4-5.4L0 4h4.2z" fill="#fff"/></svg>Welcome to Workplace Guidance Hub</h1>
      <div class="welcome-body">
        <span class="welcome-photo" role="img" aria-label="Portrait photo of the hub host"></span>
        <p class="welcome-text">Lorem ipsum dolor sit amet, consectetur adipiscing elit, sed do eiusmod tempor incididunt ut labore et dolore magna aliqua. Ut enim ad minim veniam, quis nostrud exercitation ullamco laboris.</p>
      </div>
    </section>

    <div class="columns">
      <section class="panel">
        <h2 class="panel-head whats-new"><svg width="14" height="12" viewBox="0 0 14 12"><path d="M1 1h12v8H5l-3 3V9H1z" fill="#fff"/></svg>What's new</h2>
        <article class="update"><span class="update-thumb" role="img" aria-label="News thumbnail photo"></span><div><p class="update-date">11/11/2013</p><p class="update-text">Lorem ipsum dolor sit amet, consectetur adipiscing elit, sed do eiusmod.</p></div></article>
        <article class="update"><span class="update-thumb" role="img" aria-label="News thumbnail photo"></span><div><p class="update-date">11/11/2013</p><p class="update-text">Lorem ipsum dolor sit amet, consectetur adipiscing elit, sed do eiusmod.</p></div></article>
        <article class="update"><span class="update-thumb" role="img" aria-label="News thumbnail photo"></span><div><p class="update-date">11/11/2013</p><p class="update-text">Lorem ipsum dolor sit amet, consectetur adipiscing elit, sed do eiusmod.</p></div></article>
        <article class="update"><span class="update-thumb" role="img" aria-label="News thumbnail photo"></span><div><p class="update-date">11/11/2013</p><p class="update-text">Lorem ipsum dolor sit amet, consectetur adipiscing elit, sed do eiusmod.</p></div></article>
        <article class="update"><span class="update-thumb" role="img" aria-label="News thumbnail photo"></span><div><p class="update-date">11/11/2013</p><p class="update-text">Lorem ipsum dolor sit amet, consectetur adipiscing elit, sed do eiusmod.</p></div></article>
        <article class="update"><span class="update-thumb" role="img" aria-label="News thumbnail photo"></span><div><p class="update-date">11/11/2013</p><p class="update-text">Lorem ipsum dolor sit amet, consectetur adipiscing elit, sed do eiusmod.</p></div></article>
      </section>

      <section class="panel">
        <h2 class="panel-head game"><svg width="12" height="12" viewBox="0 0 12 12"><circle cx="6" cy="3.5" r="3" fill="#fff"/><path d="M0 12a6 5 0 0 1 12 0z" fill="#fff"/></svg>Compliance game center</h2>
        <div class="feature"><div class="feature-head"><svg class="feature-icon" viewBox="0 0 22 22" fill="none" stroke="currentColor" stroke-width="1.6"><circle cx="11" cy="9" r="6"/><path d="M11 15v5M7 20h8"/></svg>Use Preferences</div><p class="feature-text">Lorem ipsum dolor sit amet, ad sit consectetur elit dolor sed tempor.</p></div>
        <div class="feature"><div class="feature-head"><svg class="feature-icon" viewBox="0 0 22 22" fill="none" stroke="currentColor" stroke-width="1.6"><rect x="2" y="3" width="18" height="12" rx="1"/><path d="M8 19h6M11 15v4M6 9l3 2 4-4 3 2"/></svg>Real Time Updates</div><p class="feature-text">Lorem ipsum dolor sit amet, ad sit consectetur elit dolor sed tempor.</p></div>
        <div class="feature"><div class="feature-head"><svg class="feature-icon" viewBox="0 0 22 22" fill="none" stroke="currentColor" stroke-width="1.6"><rect x="4" y="2" width="14" height="18" rx="1"/><path d="M7 7h8M7 11h8M7 15h6"/></svg>Team Standings</div><p class="feature-text">Lorem ipsum dolor sit amet, ad sit consectetur elit dolor sed tempor.</p></div>
        <div class="feature"><div class="feature-head"><svg class="feature-icon" viewBox="0 0 22 22" fill="none" stroke="currentColor" stroke-width="1.6"><path d="M11 3a6 6 0 0 0-3 11v3h6v-3a6 6 0 0 0-3-11zM9 20h4"/></svg>Earn Bonus Points</div><p class="feature-text">Lorem ipsum dolor sit amet, ad sit consectetur elit dolor sed tempor.</p></div>
      </section>
    </div>
  </main>

  <aside class="leaderboard">
    <h2 class="board-title">Leaderboard</h2>
    <div class="board-cols"><span>rank</span><span>player</span><span>%</span><span>score</span></div>
    <div class="board-list">
      <div class="board-row"><span class="rank">1</span><span>Marcus, T</span><span>92%</span><span>5063</span></div>
      <div class="board-row"><span class="rank">2</span><span>Alina, R</span><span>92%</span><span>5063</span></div>
      <div class="board-row"><span class="rank">3</span><span>Marcus, T</span><span>92%</span><span>5063</span></div>
      <div class="board-row"><span class="rank">4</span><span>Alina, R</span><span>92%</span><span>5063</span></div>
      <div class="board-row"><span class="rank">5</span><span>Marcus, T</span><span>92%</span><span>5063</span></div>
      <div class="board-row"><span class="rank">6</span><span>Marcus, T</span><span>92%</span><span>5063</span></div>
      <div class="board-row"><span class="rank">7</span><span>Alina, R</span><span>92%</span><span>5063</span></div>
      <div class="board-row"><span class="rank">8</span><span>Marcus, T</span><span>92%</span><span>5063</span></div>
      <div class="board-row"><span class="rank">9</span><span>Alina, R</span><span>92%</span><span>5063</span></div>
      <div class="board-row"><span class="rank">10</span><span>Marcus, T</span><span>92%</span><span>5063</span></div>
      <div class="board-row"><span class="rank">11</span><span>Alina, R</span><span>92%</span><span>5063</span></div>
      <div class="board-row"><span class="rank">12</span><span>Marcus, T</span><span>92%</span><span>5063</span></div>
      <div class="board-row"><span class="rank">13</span><span>Alina, R</span><span>92%</span><span>5063</span></div>
      <div class="board-row"><span class="rank">14</span><span>Marcus, T</span><span>92%</span><span>5063</span></div>
      <div class="board-row"><span class="rank">15</span><span>Marcus, T</span><span>92%</span><span>5063</span></div>
      <div class="board-row"><span class="rank">16</span><span>Alina, R</span><span>92%</span><span>5063</span></div>
      <div class="board-row"><span class="rank">17</span><span>Marcus, T</span><span>92%</span><span>5063</span></div>
      <div class="board-row"><span class="rank">18</span><span>Alina, R</span><span>92%</span><span>5063</span></div>
      <div class="board-row"><span class="rank">19</span><span>Marcus, T</span><span>92%</span><span>5063</span></div>
      <div class="board-row"><span class="rank">20</span><span>Alina, R</span><span>92%</span><span>5063</span></div>
      <div class="board-row"><span class="rank">21</span><span>Marcus, T</span><span>92%</span><span>5063</span></div>
      <div class="board-row"><span class="rank">22</span><span>Marcus, T</span><span>92%</span><span>5063</span></div>
      <div class="board-row"><span class="rank">23</span><span>Alina, R</span><span>92%</span><span>5063</span></div>
      <div class="board-row"><span class="rank">24</span><span>Marcus, T</span><span>92%</span><span>5063</span></div>
    </div>
  </aside>
</div>
</body>
</html>
```